Corvella Flood Restoration needing website

Hi Team

We are looking for a 4 or 5 page website containing
1: Home
2: Services
3: Gallery
4: Equipment Hire
5 Contact Us

Would want the front page to be a big call to action. Someones house has just flooded...they're highly stressed and we just want to let them know straight away that we can assist them

Some call to action would be great.

"Wet Carpets??"

"Washing machine just overflowed??"

"Burst pipe?"

"We're here to help!!"

Would be wanting a scrolling banner type homepage with images of flooded houses, heavy rain, a mother in shock that the house has been flooded by an overflowing washing machine, someone taking an emergency call with text saying that we are there to take your call 24/7 365 days a year

Target Market(s)

insurance companies and home owners

Industry/Entity Type

Hire

Coding

Coded - Design and coding required

Number of Pages Required

5+ page

Requirements
Must have
• 24/7 emergency contact number on home page (0468215937)
• 4 photos on banner on home page
• Equipment Hire Page should include images and brief description of these 3 products
• http://www.brintagesupply.com.au/item574.htm
• http://www.valdrix-tools.com.au/product/fresh-gust-fanunit/
• http://www.strellon.com.au/carpet/carpet-extractor-nomad-ser-i-ser-ii-ser-iii
• SERVICES OFFERED ARE:
• 24/7 Emergnecy Flood Restoration
• Insurance Claims
• Structural Drying
• Sub Floor Drying
• Supply and installation of drying equipment
• Professional Carpet and underlay installation
Nice to have
• Some other websites we like
• www.quillbyleakcare.com.au
• www.harrowdenrepairservices.com.au/flood-water-damage-restoration
• http://www.pelmarrecovery.com.au/
• http://www.drywellremedygroup.com.au/
Should not have
• not looking for an all white background.

```html
<!DOCTYPE html>
<html lang="en">
<head>
<meta charset="utf-8">
<title>Corvella Flood Restoration</title>
<link href="https://fonts.googleapis.com/css2?family=Montserrat:wght@400;500;600&family=Open+Sans:wght@400;600&family=Arimo&display=swap" rel="stylesheet">
<style>
:root{
  --brand:#1e88c8;
  --brand-dark:#0f5f96;
  --aqua:#2fa3d6;
  --deep:#0d5f94;
  --sky:#a6d8ec;
  --light:#f4f4f4;
  --ink:#4a4a4a;
  --white:#ffffff;
}
*{margin:0;padding:0;box-sizing:border-box}
html,body{width:1200px;height:2848px;overflow:hidden;background:var(--light)}
body{font-family:"Montserrat",sans-serif;color:var(--ink)}
.page{position:relative;width:1200px;height:2848px;overflow:hidden}
.abs{position:absolute}

/* header */
.site-header{position:absolute;top:0;left:0;width:1200px;height:90px;z-index:5}
.brand{position:absolute;left:80px;top:24px;display:flex;align-items:center;gap:12px}
.brand-dot{width:30px;height:30px;border-radius:50%;background:var(--brand)}
.brand-name{font-family:"Montserrat",sans-serif;font-weight:600;font-size:26px;color:var(--brand);letter-spacing:.5px}
.main-nav{position:absolute;right:80px;top:36px;display:flex;gap:38px;font-size:16px;font-weight:500;color:#222}
.main-nav .active{color:var(--brand)}

/* hero */
.hero-photo{position:absolute;left:0;top:0;width:1200px;height:700px;
  background:linear-gradient(180deg,#e8f0f2 0%,#c9dfe3 22%,#8fc6cf 45%,#6fb3bd 70%,#5aa0aa 100%)}
.hero-title{position:absolute;top:222px;left:0;width:1200px;text-align:center;color:var(--white);
  font-weight:600;font-size:60px;line-height:70px;letter-spacing:1px}
.hero-phone{position:absolute;top:385px;left:0;width:1200px;text-align:center;color:var(--white);font-size:36px;font-weight:500}
.btn{display:inline-block;background:var(--aqua);color:var(--white);font-weight:500;border-radius:30px;text-align:center}
.hero-cta{position:absolute;top:482px;left:483px;width:234px;height:58px;line-height:54px;font-size:22px;border:3px solid var(--white)}

/* services */
.services{position:absolute;top:660px;left:0;width:1200px;height:900px;
  background:linear-gradient(180deg,#58c0e6 0%,#2ea4d8 30%,#1b86c0 65%,#0c5d93 100%)}
.section-title{position:absolute;left:0;width:1200px;text-align:center;font-weight:500;font-size:38px;letter-spacing:1px}
.services .section-title{top:92px;color:var(--white)}
.service{position:absolute;width:320px;text-align:center;color:var(--white)}
.service-icon{width:126px;height:126px;border-radius:50%;background:var(--white);margin:0 auto;display:flex;align-items:center;justify-content:center}
.service-name{font-size:21px;line-height:27px;margin-top:28px;font-weight:400}
.service-text{font-family:"Arimo",sans-serif;font-size:14px;line-height:23px;margin-top:4px}

/* equipment */
.equipment .section-title{top:1605px;color:var(--brand)}
.product{position:absolute;top:1665px;width:300px;text-align:center}
.product-image{width:170px;height:170px;margin:0 auto;border-radius:8px}
.product-name{font-family:"Open Sans",sans-serif;font-size:17px;color:var(--brand);margin-top:22px}
.product-price{font-family:"Open Sans",sans-serif;font-size:19px;color:#555;margin-top:8px}
.hire-cta{position:absolute;top:1930px;left:486px;width:228px;height:50px;line-height:50px;font-size:21px}

/* gallery */
.gallery-band{position:absolute;top:2040px;left:0;width:1200px;height:630px;background:var(--sky)}
.gallery .section-title{top:2127px;color:var(--brand)}
.tile{position:absolute}

/* footer */
.site-footer{position:absolute;top:2670px;left:0;width:1200px;height:178px;background:var(--light)}
.footer-brand{position:absolute;left:118px;top:48px;display:flex;align-items:center;gap:10px}
.footer-brand .brand-name{font-size:22px}
.footer-brand .brand-dot{width:24px;height:24px}
.copyright{position:absolute;left:86px;top:104px;width:320px;font-size:13px;line-height:24px;text-align:center;color:#333}
.copyright span{color:var(--brand)}
.contact-list{position:absolute;left:456px;top:40px;font-family:"Open Sans",sans-serif;font-size:14px;color:#444}
.contact-item{display:flex;gap:16px;align-items:flex-start;margin-bottom:22px;line-height:22px}
.contact-item svg{flex:none;margin-top:2px}
.follow{position:absolute;left:860px;top:56px;width:200px;text-align:center;font-size:17px;color:#555;letter-spacing:1px}
.social{display:flex;gap:10px;justify-content:center;margin-top:20px}
.social i{width:40px;height:40px;border-radius:50%;background:#d5d5d5;display:block}
.social i.first{background:#3b5a9e}
</style>
</head>
<body>
<div class="page">

  <div class="hero-photo" role="img" aria-label="Photo of a living room half under clear flood water, with sofa, potted plant and lamp"></div>

  <header class="site-header">
    <div class="brand"><span class="brand-dot"></span><span class="brand-name">Corvella Flood Restoration</span></div>
    <nav class="main-nav">
      <span class="active">HOME</span><span>SERVICES</span><span>GALLERY</span><span>EQUIPMENT HIRE</span><span>CONTACT</span>
    </nav>
  </header>

  <h1 class="hero-title">"WASHING MACHINE JUST<br>OVERFLOWED??"</h1>
  <p class="hero-phone">24/7 EMERGENCY NO : (0468215937)</p>
  <a class="btn hero-cta">CONTACT NOW</a>

  <section class="services">
    <svg class="abs" style="top:0;left:0" width="1200" height="80" viewBox="0 0 1200 80" aria-hidden="true">
      <path d="M0 0H1200V20C900 -10 600 80 0 40Z" fill="#5aa0aa"/>
      <path d="M0 40C600 80 900 -10 1200 20" fill="none" stroke="#fff" stroke-width="6"/>
      <path d="M0 52C600 92 900 2 1200 32" fill="none" stroke="#1e88c8" stroke-width="6"/>
    </svg>
    <h2 class="section-title">SERVICES</h2>

    <div class="service" style="left:65px;top:170px">
      <div class="service-icon"><svg width="56" height="56" viewBox="0 0 56 56"><circle cx="28" cy="28" r="22" fill="none" stroke="#1e88c8" stroke-width="5"/><path d="M28 16V29H38" fill="none" stroke="#1e88c8" stroke-width="5"/></svg></div>
      <p class="service-name">24/7 Emergency Flood<br>Restoration</p>
      <p class="service-text">Lorem Ipsum is simply dummy text of the printing and typesetting industry. Lorem Ipsum has been the industry...</p>
    </div>
    <div class="service" style="left:440px;top:170px">
      <div class="service-icon"><svg width="60" height="60" viewBox="0 0 60 60"><path d="M6 28A24 22 0 0 1 54 28Z" fill="#1e88c8"/><path d="M30 28V50" stroke="#1e88c8" stroke-width="4"/><rect x="14" y="40" width="8" height="14" fill="#1e88c8"/><rect x="38" y="36" width="8" height="18" fill="#1e88c8"/></svg></div>
      <p class="service-name">Insurance Claims</p>
      <p class="service-text">Lorem Ipsum is simply dummy text of the printing and typesetting industry. Lorem Ipsum has been the industry...</p>
    </div>
    <div class="service" style="left:815px;top:170px">
      <div class="service-icon"><svg width="60" height="60" viewBox="0 0 60 60"><path d="M10 40A20 20 0 1 1 50 40" fill="none" stroke="#1e88c8" stroke-width="5"/><path d="M30 32L40 18" stroke="#1e88c8" stroke-width="4"/><path d="M40 36C40 36 32 46 40 52C48 46 40 36 40 36Z" fill="#1e88c8"/></svg></div>
      <p class="service-name">Structural Drying</p>
      <p class="service-text">Lorem Ipsum is simply dummy text of the printing and typesetting industry. Lorem Ipsum has been the industry...</p>
    </div>

    <div class="service" style="left:65px;top:482px">
      <div class="service-icon"><svg width="56" height="60" viewBox="0 0 56 60"><rect x="14" y="6" width="30" height="48" rx="4" fill="none" stroke="#1e88c8" stroke-width="4"/><path d="M24 18C24 18 14 32 24 38C34 32 24 18 24 18Z" fill="#1e88c8"/></svg></div>
      <p class="service-name">Sub Floor Drying</p>
      <p class="service-text">Lorem Ipsum is simply dummy text of the printing and typesetting industry. Lorem Ipsum has been the industry...</p>
    </div>
    <div class="service" style="left:440px;top:482px">
      <div class="service-icon"><svg width="60" height="50" viewBox="0 0 60 50"><rect x="10" y="10" width="34" height="28" rx="4" fill="#1e88c8"/><rect x="44" y="20" width="10" height="8" fill="#1e88c8"/><rect x="6" y="40" width="42" height="5" fill="#1e88c8"/></svg></div>
      <p class="service-name">Supply and installation of<br>drying equipment</p>
      <p class="service-text">Lorem Ipsum is simply dummy text of the printing and typesetting industry. Lorem Ipsum has been the industry...</p>
    </div>
    <div class="service" style="left:815px;top:482px">
      <div class="service-icon"><svg width="60" height="60" viewBox="0 0 60 60"><circle cx="22" cy="24" r="14" fill="#1e88c8"/><path d="M22 38H50L44 50H16Z" fill="#1e88c8"/></svg></div>
      <p class="service-name">Professional Carpet and<br>underlay installation</p>
      <p class="service-text">Lorem Ipsum is simply dummy text of the printing and typesetting industry. Lorem Ipsum has been the industry...</p>
    </div>
  </section>

  <svg class="abs" style="top:1470px;left:0" width="1200" height="90" viewBox="0 0 1200 90" aria-hidden="true">
    <path d="M0 0V60C300 100 700 10 1200 50V90H0Z" fill="#f4f4f4"/>
    <path d="M0 60C300 100 700 10 1200 50" fill="none" stroke="#1e88c8" stroke-width="6"/>
    <path d="M0 72C300 112 700 22 1200 62" fill="none" stroke="#fff" stroke-width="5"/>
  </svg>

  <section class="equipment">
    <h2 class="section-title">EQUIPMENT HIRE</h2>
    <div class="product" style="left:96px">
      <div class="product-image" role="img" aria-label="Photo of a blue portable dehumidifier" style="background:linear-gradient(160deg,#3f9fcf,#2b6f96 60%,#444)"></div>
      <p class="product-name">DEHUMIDIFIER KX 2500 230VOLT</p>
      <p class="product-price">$ 330</p>
    </div>
    <div class="product" style="left:450px">
      <div class="product-image" role="img" aria-label="Photo of a white carpet extractor machine" style="background:linear-gradient(160deg,#f0f0f0,#d4d4d4 60%,#b03030)"></div>
      <p class="product-name">NOMAD</p>
      <p class="product-price">$ 370</p>
    </div>
    <div class="product" style="left:828px">
      <div class="product-image" role="img" aria-label="Photo of stacked blue air mover fans" style="background:linear-gradient(160deg,#3a6fd6,#1c3fa3)"></div>
      <p class="product-name">FRESH GUST AIRMOVER</p>
      <p class="product-price">$ 405</p>
    </div>
    <a class="btn hire-cta">HIRE US NOW</a>
  </section>

  <section class="gallery">
    <div class="gallery-band"></div>
    <svg class="abs" style="top:2010px;left:0" width="1200" height="110" viewBox="0 0 1200 110" aria-hidden="true">
      <path d="M0 50C350 110 700 -10 1200 40V110H0Z" fill="#a6d8ec"/>
      <path d="M0 48C350 108 700 -12 1200 38" fill="none" stroke="#1e88c8" stroke-width="6"/>
      <path d="M0 62C350 122 700 2 1200 52" fill="none" stroke="#fff" stroke-width="5"/>
    </svg>
    <h2 class="section-title">GALLERY</h2>
    <div class="tile" style="left:78px;top:2202px;width:250px;height:326px;background:linear-gradient(180deg,#cfd6da,#f3f3f3 55%,#b9b2aa)" role="img" aria-label="Photo of a washing machine overflowing with foam"></div>
    <div class="tile" style="left:343px;top:2202px;width:515px;height:156px;background:linear-gradient(90deg,#8d6a44,#b88b5a 50%,#7a5a3a)" role="img" aria-label="Photo of workers lifting damaged floorboards"></div>
    <div class="tile" style="left:872px;top:2202px;width:250px;height:156px;background:linear-gradient(135deg,#e6e2dc,#c9c4bc)" role="img" aria-label="Photo of a wall opened up to show burst pipes"></div>
    <div class="tile" style="left:343px;top:2372px;width:250px;height:156px;background:linear-gradient(180deg,#b9b0a2,#6f7f95)" role="img" aria-label="Photo of a man catching a ceiling leak in a bucket"></div>
    <div class="tile" style="left:607px;top:2372px;width:515px;height:156px;background:linear-gradient(180deg,#d9d4cc,#8a8f94 60%,#3e4348)" role="img" aria-label="Photo of a flooded living room with a white sofa"></div>
  </section>

  <svg class="abs" style="top:2600px;left:0;z-index:2" width="1200" height="90" viewBox="0 0 1200 90" aria-hidden="true">
    <path d="M0 60C400 90 800 20 1200 50V90H0Z" fill="#f4f4f4"/>
    <path d="M0 56C400 86 800 16 1200 46" fill="none" stroke="#1e88c8" stroke-width="6"/>
  </svg>

  <footer class="site-footer">
    <div class="footer-brand"><span class="brand-dot"></span><span class="brand-name">Corvella Flood Restoration</span></div>
    <p class="copyright">© <span>CORVELLA FLOOD RESTORATION</span> - 2016. All Rights Reserved.</p>
    <div class="contact-list">
      <div class="contact-item"><svg width="18" height="22" viewBox="0 0 18 22"><path d="M9 0A8 8 0 0 1 17 8C17 14 9 22 9 22C9 22 1 14 1 8A8 8 0 0 1 9 0Z" fill="#1e88c8"/><circle cx="9" cy="8" r="3" fill="#fff"/></svg><span>123 Building Name, Street Name, City,<br>Country - Zipcode</span></div>
      <div class="contact-item"><svg width="18" height="18" viewBox="0 0 18 18"><path d="M3 1L7 1L8 6L5.5 7.5C6.5 10 8 11.5 10.5 12.5L12 10L17 11V15C17 16 16 17 15 17C7 17 1 11 1 3C1 2 2 1 3 1Z" fill="#1e88c8"/></svg><span>0468215937</span></div>
      <div class="contact-item"><svg width="18" height="14" viewBox="0 0 18 14"><rect width="18" height="14" rx="1" fill="#1e88c8"/><path d="M1 1L9 8L17 1" fill="none" stroke="#fff" stroke-width="1.5"/></svg><span>info@corvella.com</span></div>
    </div>
    <div class="follow">FOLLOW US ON:
      <div class="social"><i class="first"></i><i></i><i></i><i></i></div>
    </div>
  </footer>

</div>
</body>
</html>
```